New Business Card Design

we need a new business card as we have just moved location and need a fresh new look. we are a Land Surveying Company . the card needs to be 2 sided and needs to have what we do on the back as our previous card ( attached ).
i was thinking of maybe a ruler down the bottom of the card or something to make it stand out. size can be 90 x 55 or 90 x 45 .
maybe a shadow of the logo or something in the corner.
on the attached card where it says other offices , it should be Melbourne instead of bendigo

postal address should be there as PO box 812 , Thornbury Flats 3821
Updates

Reason: some designs didn't follow brief by having services provided on the back of the card, just giving a bit of time toi change and to review.

Industry/Entity Type

Business

Requirements
Must have
• All cards need to have services provided on the back please , as stated , a lot of designs have just had the logo on the back

```html
<!DOCTYPE html>
<html lang="en">
<head>
<meta charset="utf-8">
<title>Calder Wynne Land Surveyors – Business Card</title>
<link rel="stylesheet" href="https://fonts.googleapis.com/css2?family=Arimo:wght@400;700&display=swap">
<style>
  :root {
    --stage: #1c1c1c;
    --card: #ffffff;
    --ink: #111111;
    --band: #151515;
    --accent: #1a66c9;
    --muted: #222222;
    --on-band: #ffffff;
    --rule: #333333;
  }
  * { box-sizing: border-box; margin: 0; padding: 0; }
  html, body { width: 1200px; height: 818px; overflow: hidden; }
  body {
    background: var(--stage);
    font-family: "Arimo", Arial, sans-serif;
    position: relative;
  }
  .card {
    position: absolute;
    top: 256px;
    width: 500px;
    height: 306px;
    background: var(--card);
    overflow: hidden;
    box-shadow: 0 10px 30px rgba(0,0,0,.45);
  }
  .card--services { left: 70px; }
  .card--contact { left: 630px; }
  .card__shapes { position: absolute; inset: 0; width: 100%; height: 100%; }

  .brand {
    position: absolute;
    display: flex;
    align-items: center;
    gap: 10px;
  }
  .brand__mark {
    width: 44px; height: 44px;
    border-radius: 50%;
    background: var(--accent);
    flex: none;
  }
  .brand__name, .brand__tagline {
    color: var(--ink);
    font-weight: 700;
    text-transform: uppercase;
    line-height: 1;
  }
  .brand__name { font-size: 26px; letter-spacing: .5px; }
  .brand__tagline { font-size: 12.5px; letter-spacing: 5.2px; margin-top: 5px; }

  .card--services .brand { left: 128px; top: 92px; }
  .card--contact .brand { left: 210px; top: 66px; }

  .web-link {
    position: absolute;
    left: 14px; top: 180px;
    font-size: 12px;
    color: var(--accent);
  }

  .services {
    position: absolute;
    right: 18px; top: 252px;
    list-style: none;
    text-align: right;
    font-size: 10.5px;
    line-height: 14px;
    color: var(--muted);
    width: 290px;
  }
  .services li { display: inline; }
  .services li + li::before { content: " · "; color: var(--accent); font-weight: 700; }

  .person { position: absolute; left: 26px; top: 128px; }
  .person__name { font-size: 19px; color: var(--accent); font-weight: 400; }
  .person__role { font-size: 11px; color: var(--muted); margin-top: 3px; }
  .person__contact { font-size: 11.5px; color: var(--muted); margin-top: 14px; line-height: 1.45; }

  .band-contact {
    position: absolute;
    right: 22px; top: 250px;
    font-size: 11.5px;
    line-height: 1.5;
    color: var(--on-band);
  }
</style>
</head>
<body>

  <section class="card card--services" aria-label="Card back with services">
    <svg class="card__shapes" viewBox="0 0 500 306" aria-hidden="true">
      <polygon points="0,200 200,200 176,236 0,236" fill="var(--band)"/>
      <polygon points="0,236 176,236 168,248 0,248" fill="var(--accent)"/>
      <polygon points="400,0 500,0 500,78" fill="var(--band)"/>
      <polygon points="386,0 400,0 500,78 500,90" fill="var(--accent)"/>
      <g class="ruler" stroke="var(--rule)" stroke-width="1">
        <line x1="0" y1="305.5" x2="500" y2="305.5"/>
        <path d="M10 306v-12M20 306v-5M30 306v-5M40 306v-5M50 306v-8M60 306v-5M70 306v-5M80 306v-5M90 306v-5M100 306v-12M110 306v-5M120 306v-5M130 306v-5M140 306v-5M150 306v-8M160 306v-5M170 306v-5M180 306v-5M190 306v-5M200 306v-12M210 306v-5M220 306v-5M230 306v-5M240 306v-5M250 306v-8M260 306v-5M270 306v-5M280 306v-5M290 306v-5M300 306v-12M310 306v-5M320 306v-5M330 306v-5M340 306v-5M350 306v-8M360 306v-5M370 306v-5M380 306v-5M390 306v-5M400 306v-12M410 306v-5M420 306v-5M430 306v-5M440 306v-5M450 306v-8M460 306v-5M470 306v-5M480 306v-5M490 306v-5"/>
      </g>
    </svg>
    <div class="brand">
      <span class="brand__mark"></span>
      <div>
        <div class="brand__name">Calder Wynne</div>
        <div class="brand__tagline">Land Surveyors</div>
      </div>
    </div>
    <p class="web-link">www.calderwynne.com.au</p>
    <ul class="services" aria-label="Services">
      <li>Subdivisions</li><li>Boundary Surveys</li><li>Title Re-establishment</li><li>Feature &amp; Level Surveys</li><li>Construction Set Out</li>
    </ul>
  </section>

  <section class="card card--contact" aria-label="Card front with contact details">
    <svg class="card__shapes" viewBox="0 0 500 306" aria-hidden="true">
      <polygon points="0,0 56,0 0,36" fill="var(--band)"/>
      <polygon points="56,0 68,0 0,44 0,36" fill="var(--accent)"/>
      <polygon points="300,236 500,236 500,306 286,306" fill="var(--band)"/>
      <polygon points="288,236 300,236 286,306 272,306" fill="var(--accent)"/>
    </svg>
    <div class="brand">
      <span class="brand__mark"></span>
      <div>
        <div class="brand__name">Calder Wynne</div>
        <div class="brand__tagline">Land Surveyors</div>
      </div>
    </div>
    <div class="person">
      <h1 class="person__name">Martin Wynne</h1>
      <p class="person__role">Director</p>
      <p class="person__contact">Call: 0412 558301<br>PO box 812 , Thornbury Flats 3821</p>
    </div>
    <p class="band-contact">info@calderwynne.com.au<br>www.calderwynne.com.au</p>
  </section>

</body>
</html>
```